Vornique Business Cards

We need new business cards that incorporate our new compnay logo and color scheme. We are a custom publishing company located in Brookvale, WI.

Target Market(s)

Deans, Assistant Deans, Executive MBA Program Directors and Faculty at top universities in North America. Top publishers in North America.

Industry/Entity Type

Publishing Company

Requirements
Must have
• The Vornique Logo
The following color palatte:
Gold:
C: 1
M: 6
Y: 25
K: 0

Darker gold
C: 0
M: 31
Y: 100
K: 0

Purple
C: 78
M: 100
Y: 0
K: 33

Teal
C: 87
M: 0
Y: 38
K: 0

Must also be able to fit the following sample b-card information:
www.vornique-example.com
Priya Ostrander
Director, Marketing
2315 Harrow Lane, PO Box 417
Ann Arbor, MI 48213-0417
phone: 800-555-0143 x2291
email: postrander@vornique-example.com
Nice to have
• match the look and feel of our website: www.vornique-example.com

```html
<!DOCTYPE html>
<html lang="en">
<head>
<meta charset="utf-8">
<title>Vornique Business Card</title>
<link rel="stylesheet" href="https://fonts.googleapis.com/css2?family=Jost:wght@400;500;600&display=swap">
<style>
  :root {
    --purple: #2b00a2;
    --purple-deep: #17005e;
    --gold: #f7a823;
    --teal: #3ee6b0;
    --teal-light: #8ff5d2;
    --white: #ffffff;
    --paper: #ffffff;
  }
  * { margin: 0; padding: 0; box-sizing: border-box; }
  html, body {
    width: 1005px;
    height: 1200px;
    overflow: hidden;
    background: var(--paper);
    font-family: "Jost", sans-serif;
  }
  .sheet { position: relative; width: 1005px; height: 1200px; }

  .card {
    position: absolute;
    left: 0;
    width: 1005px;
    height: 556px;
    background: var(--purple);
    overflow: hidden;
  }
  .card--front { top: 0; }
  .card--back { top: 641px; height: 559px; width: 1002px; }

  .card__art { position: absolute; inset: 0; }

  .card__url {
    position: absolute;
    color: var(--gold);
    font-size: 25px;
    font-weight: 400;
    letter-spacing: 0.5px;
    white-space: nowrap;
  }
  .card--front .card__url { right: 56px; top: 14px; }
  .card--back .card__url { left: 0; right: 0; top: 415px; text-align: center; }

  .person__name {
    position: absolute;
    left: 0;
    width: 785px;
    top: 136px;
    text-align: right;
    color: var(--white);
    font-size: 64px;
    font-weight: 600;
    white-space: nowrap;
  }
  .person__rule {
    position: absolute;
    left: 5px;
    top: 222px;
    width: 790px;
    height: 4px;
    background: var(--gold);
  }
  .person__title {
    position: absolute;
    left: 312px;
    top: 236px;
    color: var(--white);
    font-size: 42px;
    font-weight: 400;
    white-space: nowrap;
  }

  .contact {
    position: absolute;
    left: 532px;
    top: 380px;
    list-style: none;
    color: var(--white);
    font-size: 23px;
    line-height: 34px;
    letter-spacing: 0.3px;
    white-space: nowrap;
  }

  .brand {
    position: absolute;
    left: 46px;
    top: 440px;
    display: flex;
    align-items: center;
    gap: 12px;
  }
  .brand__dot {
    width: 26px;
    height: 26px;
    border-radius: 50%;
    background: var(--teal);
  }
  .brand__name {
    color: var(--teal);
    font-size: 44px;
    font-weight: 500;
    line-height: 1;
  }
</style>
</head>
<body>
<main class="sheet">
  <section class="card card--front">
    <svg class="card__art" width="1005" height="556" viewBox="0 0 1005 556">
      <defs>
        <linearGradient id="edgeShade" x1="0" y1="0" x2="1" y2="0.6">
          <stop offset="0" stop-color="var(--purple)" stop-opacity="0"/>
          <stop offset="1" stop-color="var(--purple-deep)"/>
        </linearGradient>
        <radialGradient id="swirlTone" cx="0.75" cy="0.2" r="0.8">
          <stop offset="0" stop-color="var(--teal-light)"/>
          <stop offset="1" stop-color="var(--teal)"/>
        </radialGradient>
      </defs>
      <path class="card__shade" d="M470 0 C 640 90 860 230 1005 420 L1005 0 Z" fill="url(#edgeShade)"/>
      <path class="card__swirl-field" role="img" aria-label="Decorative teal swirl pattern"
            d="M555 0 C 760 90 910 230 1005 392 L1005 0 Z" fill="url(#swirlTone)"/>
    </svg>

    <p class="card__url">www.vornique-example.com</p>

    <h1 class="person__name">Priya Ostrander</h1>
    <div class="person__rule"></div>
    <p class="person__title">Director, Marketing</p>

    <ul class="contact">
      <li>2315 Harrow Lane, PO Box 417</li>
      <li>Brookvale, WI 48213-0417</li>
      <li>phone: 800-555-0143 x2291</li>
      <li>email: postrander@vornique-example.com</li>
    </ul>

    <div class="brand">
      <span class="brand__dot"></span>
      <span class="brand__name">Vornique</span>
    </div>
  </section>

  <section class="card card--back">
    <p class="card__url">www.vornique-example.com</p>
  </section>
</main>
</body>
</html>
```